Steel Company / Iron Railing Business Card Template

We are a custom steel fabrication company located in Harlow Ferry, ST. In business since 1979, we recently developed a new logo, and we're looking for a business card design to help display the new logo and our business. The name of the company is Kelbrook Forge Co.. The Office Phone number is (610) 555-0143. We fabricate and install custom "wrought iron" railings on our residential side, we also fabricate and erect structural steel (think cranes and steel beams in buildings) on our commercial side. Looking to get a business card template designed. Something modern, but professional. Clear and easy to read. Front should have all business and employee information including phone number(s), email address, business information, etc. back should spotlight logo.

Industry/Entity Type

Construction / Home Improvement

Contact Information for Business Card

Business information is Kelbrook Forge Co., 48 Dunmore Ave Suite 3305, Harlow Ferry, ST 19074. Phone number is (610) 555-0143. Website is www.kelbrookforge.example Business card should be for "Tom Pelling" with the job title "Sales & Estimating" but be editable for other employees. Tom's phone number is (610) 555-0178

Colors

Designer to choose colors to be used in the design.

Requirements
Must have
• Modern Feel, Design should be sized for standard business card sizing 3.5" x 2" (88.9mm x 50.8mm)

```html
<!DOCTYPE html>
<html lang="en">
<head>
<meta charset="utf-8">
<title>Kelbrook Forge Co. – Business Card</title>
<link href="https://fonts.googleapis.com/css2?family=Figtree:wght@400;600;800&display=swap" rel="stylesheet">
<style>
  :root {
    --page-bg: #e9eaec;
    --brand-blue: #22397f;
    --brand-blue-deep: #1f3475;
    --brand-red: #d23a3a;
    --paper-white: #f5f5f5;
    --ink-light: #e6eaf4;
  }
  * { box-sizing: border-box; margin: 0; padding: 0; }
  html, body {
    width: 1200px; height: 1200px; overflow: hidden;
    background: var(--page-bg);
    font-family: "Figtree", "Helvetica Neue", Arial, sans-serif;
  }
  .sheet { position: relative; width: 1200px; height: 1200px; }
  .card {
    position: absolute; top: 216px;
    width: 416px; height: 728px;
    background: linear-gradient(180deg, var(--brand-blue) 0%, var(--brand-blue-deep) 100%);
    border-radius: 4px;
    overflow: hidden;
  }
  .card-front { left: 134px; }
  .card-back { left: 611px; }

  /* Front */
  .front-header {
    height: 186px; background: var(--paper-white);
    display: flex; align-items: flex-end; justify-content: center;
    padding-bottom: 22px;
  }
  .brand-name {
    font-weight: 800; font-size: 32px; letter-spacing: 0.3px;
    color: var(--brand-blue);
  }
  .front-body {
    text-align: center; color: var(--ink-light);
    padding-top: 180px;
  }
  .person-name {
    font-weight: 600; font-size: 25px; color: #fff; line-height: 1.1;
  }
  .person-title { font-size: 18px; margin-top: 6px; letter-spacing: 0.3px; }
  .contact-icons {
    display: flex; justify-content: center; gap: 8px; margin-top: 30px;
  }
  .contact-icons svg { width: 17px; height: 17px; }
  .contact-list {
    list-style: none; margin-top: 8px; font-size: 18px; line-height: 26px;
    letter-spacing: 0.2px;
  }
  .divider {
    width: 80px; height: 2px; background: var(--ink-light);
    margin: 20px auto 18px;
  }
  .address { font-size: 18px; line-height: 26px; letter-spacing: 0.2px; }

  /* Back */
  .back-inner {
    position: absolute; width: 728px; height: 416px;
    left: -156px; top: 156px;
    transform: rotate(-90deg);
    text-align: center; color: var(--ink-light);
  }
  .back-brand {
    position: absolute; left: 0; right: 0; top: 104px;
    font-weight: 800; font-size: 34px; color: #fff; line-height: 1.1;
  }
  .services-heading {
    position: absolute; left: 0; right: 0; top: 256px;
    font-weight: 600; font-size: 17px; color: #fff;
  }
  .services-rule {
    position: absolute; left: 308px; width: 112px; top: 284px;
    height: 2px; background: var(--ink-light);
  }
  .services-list {
    position: absolute; left: 10px; right: 10px; top: 294px;
    font-size: 16px; line-height: 23px; letter-spacing: 0.2px;
  }
  .bullet { color: var(--brand-red); margin: 0 5px; font-size: 13px; }
</style>
</head>
<body>
<div class="sheet">

  <section class="card card-front">
    <header class="front-header">
      <span class="brand-name">Kelbrook Forge Co.</span>
    </header>
    <div class="front-body">
      <h1 class="person-name">Tom Pelling</h1>
      <p class="person-title">Sales &amp; Estimating</p>

      <div class="contact-icons" aria-hidden="true">
        <svg viewBox="0 0 24 24" fill="none" stroke="#fff" stroke-width="2" stroke-linecap="round" stroke-linejoin="round">
          <path d="M5 3h4l2 5-3 2a11 11 0 0 0 6 6l2-3 5 2v4a2 2 0 0 1-2 2A17 17 0 0 1 3 5a2 2 0 0 1 2-2z"/>
        </svg>
        <svg viewBox="0 0 24 24" fill="none" stroke="#fff" stroke-width="2">
          <rect x="6" y="2" width="12" height="20" rx="2"/><line x1="11" y1="18" x2="13" y2="18"/>
        </svg>
        <svg viewBox="0 0 24 24" fill="#fff">
          <path d="M3 6h18v12H3z"/><path d="M3 6l9 7 9-7" stroke="#22397f" stroke-width="2" fill="none"/>
        </svg>
        <svg viewBox="0 0 24 24" fill="none" stroke="#fff" stroke-width="2">
          <circle cx="12" cy="12" r="9"/><path d="M3 12h18M12 3c3 3 3 15 0 18M12 3c-3 3-3 15 0 18"/>
        </svg>
      </div>

      <ul class="contact-list">
        <li>(555) 555-0143</li>
        <li>(555) 555-0178</li>
        <li>info@kelbrookforge.example</li>
        <li>www.kelbrookforge.example</li>
      </ul>

      <div class="divider"></div>

      <p class="address">48 Dunmore Ave Suite 3305,<br>Harlow Ferry, ST 19074</p>
    </div>
  </section>

  <section class="card card-back">
    <div class="back-inner">
      <div class="back-brand">Kelbrook Forge Co.</div>
      <h2 class="services-heading">Our Services</h2>
      <div class="services-rule"></div>
      <p class="services-list">
        <span class="bullet">●</span>wrought iron railings <span class="bullet">●</span>structural steel <span class="bullet">●</span>steel stairs &amp; decks <span class="bullet">●</span>iron &amp; steel gates<br>
        <span class="bullet">●</span>steel fire escapes &amp; balconies <span class="bullet">●</span>plasma cutting <span class="bullet">●</span>window guards <span class="bullet">●</span>steel stairs<br>
        <span class="bullet">●</span>balcony rails
      </p>
    </div>
  </section>

</div>
</body>
</html>
```